Stonebell Inc Ad Design, trying to attract new customers

Please see attached pictures and files for information
We are a Class A - Residential General Contractor in Lynchburg, VA with Master HVAC and Master PLUMBING Licenses. We focus on Water and Air Solutions for property owners.
We build, remodel, and repair homes
We do HVAC, including Humidity Control and Air Purification
We do Plumbing
We love to fix Water Leaks for Plumbing, Roof Leaks, Skylight Leaks, Basement Leaks, Foundation Leaks, Door and Window Leaks
We solve water and air issues on the outside of properties with custom structures, grading, and landscaping

Target Market(s)

Residential and Light Commercial property owners

Industry/Entity Type

Construction

Font styles to use
Other font styles liked:
• see cards

Colors
0054AA
0677BA
7BADD7
CADEEF
E8F1F8
00AB8E
00BBA5
67D7C9
C6EFE9
E9F9F6

Requirements
Must have
• See business cards
Nice to have
• see business cards
Should not have
• My name

```html
<!DOCTYPE html>
<html lang="en">
<head>
<meta charset="utf-8">
<title>Stonebell Inc – Billboard</title>
<link rel="stylesheet" href="https://fonts.googleapis.com/css2?family=Outfit:wght@400;600;700;800&family=Varela+Round&family=Nunito:wght@900&display=swap">
<style>
  :root {
    --page-bg: #d6d6d6;
    --white: #ffffff;
    --brand-blue: #0a6cc0;
    --deep-blue: #0054aa;
    --sky-blue: #7badd7;
    --brand-green: #4aa84a;
    --text-green: #3fae49;
    --lime: #7dc242;
    --ink: #1d1d1d;
    --photo-light: #f1ece4;
    --photo-mid: #d9cdbd;
    --photo-dark: #8f8a86;
  }
  * { margin: 0; padding: 0; box-sizing: border-box; }
  html, body { width: 980px; height: 1200px; overflow: hidden; }
  body { background: var(--page-bg); font-family: "Varela Round", sans-serif; }

  .billboard {
    position: absolute; left: 20px; top: 365px;
    width: 940px; height: 470px; overflow: hidden;
    background: var(--white);
    box-shadow: 0 6px 16px rgba(0,0,0,.18);
  }
  .billboard-art { position: absolute; inset: 0; width: 940px; height: 470px; }

  .brand {
    position: absolute; left: 88px; top: 70px;
    display: flex; align-items: center; gap: 12px;
  }
  .brand-dot { width: 26px; height: 26px; border-radius: 50%; background: var(--brand-green); }
  .brand-name {
    font-family: "Outfit", sans-serif; font-weight: 800;
    font-size: 40px; letter-spacing: 2px; color: var(--brand-blue);
  }

  .tagline {
    position: absolute; left: 53px; top: 152px;
    font-family: "Outfit", sans-serif; font-weight: 400;
    font-size: 21px; color: var(--ink);
  }
  .headline { position: absolute; left: 52px; top: 180px; font-family: "Outfit", sans-serif; font-weight: 700; line-height: 1; }
  .headline-class { display: block; font-size: 46px; color: var(--text-green); }
  .headline-trade { display: block; font-size: 50px; color: var(--brand-blue); margin-top: 0; letter-spacing: -.5px; }

  .credential {
    position: absolute; left: 656px; top: 127px; width: 284px; height: 43px;
    background: var(--brand-blue); color: var(--white);
    font-family: "Nunito", sans-serif; font-weight: 900; font-size: 21px;
    padding-left: 18px; line-height: 43px;
  }

  .services { position: absolute; left: 516px; top: 192px; list-style: none; color: var(--white); font-size: 18.5px; line-height: 22px; }
  .services li { position: relative; padding-left: 26px; margin-bottom: 12px; }
  .services li svg { position: absolute; left: 0; top: 4px; width: 15px; height: 13px; }
  .services .feature { font-family: "Nunito", sans-serif; font-weight: 900; }

  .contact { position: absolute; left: 54px; top: 348px; list-style: none; color: var(--white); }
  .contact li { display: flex; align-items: center; gap: 8px; font-size: 20.5px; height: 31px; }
  .contact .phone { font-family: "Outfit", sans-serif; font-weight: 700; font-size: 28px; height: 36px; }
  .contact svg { width: 18px; height: 18px; flex: none; }
</style>
</head>
<body>
<main class="billboard">
  <svg class="billboard-art" viewBox="0 0 940 470" aria-hidden="false">
    <defs>
      <linearGradient id="photoTone" x1="0" y1="0" x2="1" y2="0">
        <stop offset="0" stop-color="var(--photo-light)"/>
        <stop offset=".55" stop-color="var(--photo-mid)"/>
        <stop offset="1" stop-color="var(--photo-dark)"/>
      </linearGradient>
      <linearGradient id="blueBand" x1="0" y1="0" x2="1" y2="1">
        <stop offset="0" stop-color="var(--brand-blue)"/>
        <stop offset="1" stop-color="var(--deep-blue)"/>
      </linearGradient>
    </defs>
    <path role="img" aria-label="Photo of a woman relaxing on a sofa beside an air purifier"
          d="M412,0 C398,60 412,130 437,170 L940,170 L940,0 Z" fill="url(#photoTone)"/>
    <path class="service-panel" d="M437,170 L940,170 L940,340 C850,392 700,408 560,398 C520,394 490,386 462,374 C492,300 474,230 437,170 Z" fill="var(--brand-green)"/>
    <path class="lime-swoosh" d="M0,303 C120,262 280,275 420,362 C280,300 130,296 0,324 Z" fill="var(--lime)"/>
    <path class="contact-band" d="M0,322 C130,296 290,300 430,350 C600,420 820,410 940,352 L940,470 L0,470 Z" fill="url(#blueBand)"/>
    <path d="M430,352 C600,420 820,410 940,352" fill="none" stroke="var(--white)" stroke-width="5"/>
    <path d="M540,420 C700,445 840,440 940,400" fill="none" stroke="var(--white)" stroke-width="4"/>
    <ellipse cx="750" cy="420" rx="80" ry="10" fill="var(--sky-blue)" opacity=".5"/>
  </svg>

  <div class="brand">
    <span class="brand-dot"></span>
    <span class="brand-name">STONEBELL</span>
  </div>

  <p class="tagline">"We put Water and Air in its place"</p>
  <h1 class="headline">
    <span class="headline-class">Class A RBC</span>
    <span class="headline-trade">PLUMBINGHVAC</span>
  </h1>

  <div class="credential">Licensed and Insured</div>

  <ul class="services">
    <li><svg viewBox="0 0 15 13"><path d="M1,7 L5.5,11 L14,1.5" fill="none" stroke="#fff" stroke-width="2.6"/></svg>Humidity Control/Air Purification</li>
    <li><svg viewBox="0 0 15 13"><path d="M1,7 L5.5,11 L14,1.5" fill="none" stroke="#fff" stroke-width="2.6"/></svg>Roof/Skylight Leaks, Basement/<br>Foundation Leaks</li>
    <li><svg viewBox="0 0 15 13"><path d="M1,7 L5.5,11 L14,1.5" fill="none" stroke="#fff" stroke-width="2.6"/></svg>Drainage/Grading/Landscaping</li>
    <li><svg viewBox="0 0 15 13"><path d="M1,7 L5.5,11 L14,1.5" fill="none" stroke="#fff" stroke-width="2.6"/></svg><span class="feature">Custom Outdoor Structures</span><br>Porches, Decks, Sunrooms, Gazebos</li>
  </ul>

  <ul class="contact">
    <li class="phone"><svg viewBox="0 0 18 18"><path d="M4,1 L7,1 L8,5 L6,7 C7,10 8,11 11,12 L13,10 L17,11 L17,14 C17,16 15,17 13,17 C6,16 2,12 1,5 C1,3 2,1 4,1 Z" fill="#fff"/></svg>(434) 555-0187</li>
    <li><svg viewBox="0 0 18 18"><circle cx="9" cy="9" r="9" fill="#fff"/><rect x="4" y="5.5" width="10" height="7" fill="none" stroke="var(--brand-blue)" stroke-width="1.3"/><path d="M4,5.5 L9,10 L14,5.5" fill="none" stroke="var(--brand-blue)" stroke-width="1.3"/></svg>Control@StonebellVA.com</li>
    <li><svg viewBox="0 0 18 18"><circle cx="9" cy="9" r="9" fill="#fff"/><circle cx="9" cy="9" r="5.5" fill="none" stroke="var(--brand-blue)" stroke-width="1.2"/><ellipse cx="9" cy="9" rx="2.4" ry="5.5" fill="none" stroke="var(--brand-blue)" stroke-width="1.2"/><path d="M3.5,9 H14.5" stroke="var(--brand-blue)" stroke-width="1.2"/></svg>www.ShadeworksVA.com</li>
  </ul>
</main>
</body>
</html>
```